Plivora Display Ads For Women (300x250 pixel)

We need ads for plivora display. Please use the attached image to create GIF file ads. The ads needs to have the Bidmarlow logo (attatched) and the slogan "Up To 80% Off Retail". The ads should have different background variation but the product or item should be center of attention.

Dimension: 300 by 250 pixel
File Type: GIF

Target Market(s)

Women

Industry/Entity Type

Plivora

Font styles to use
Sans Serif

Requirements
Must have
• "View Now" button

```html
<!DOCTYPE html>
<html lang="en">
<head>
<meta charset="utf-8">
<title>Bidmarlow Display Ads</title>
<link rel="stylesheet" href="https://fonts.googleapis.com/css2?family=Raleway:wght@400;500&display=swap">
<style>
  :root {
    --board-light: #f3f4f6;
    --board-mid: #c9ccd1;
    --board-dark: #8f949b;
    --tile-bg: #ffffff;
    --ink: #000000;
    --ink-soft: #b9b9b9;
    --text-light: #ffffff;
    --brand-ink: #1a1a1a;
  }
  * { margin: 0; padding: 0; box-sizing: border-box; }
  html, body { width: 1200px; height: 1200px; overflow: hidden; }
  body {
    position: relative;
    background: radial-gradient(ellipse 70% 65% at 50% 45%, var(--board-light) 0%, var(--board-mid) 60%, var(--board-dark) 100%);
    font-family: "Raleway", Arial, sans-serif;
  }
  .ad {
    position: absolute;
    width: 455px;
    height: 375px;
    background: var(--tile-bg);
    overflow: hidden;
  }
  .ad--a { left: 138px; top: 18px; }
  .ad--b { left: 612px; top: 18px; }
  .ad--c { left: 138px; top: 415px; }
  .ad--d { left: 612px; top: 415px; }
  .ad--e { left: 363px; top: 811px; }

  .brand {
    position: absolute;
    left: 22px; top: 26px;
    display: flex; align-items: center; gap: 8px;
    color: var(--brand-ink);
    font-size: 29px; font-weight: 400; letter-spacing: 0.5px;
  }
  .brand__mark { width: 24px; height: 24px; background: var(--brand-ink); }

  .product {
    position: absolute;
    left: 250px; top: 50px;
    width: 190px; height: 250px;
    border-radius: 50% 50% 45% 45%;
  }
  .product--gold   { background: radial-gradient(circle at 45% 40%, #f4f4f4 0%, #d9c08a 45%, #b58a3a 75%, transparent 78%); }
  .product--noir   { background: radial-gradient(circle at 45% 40%, #e58bc9 0%, #3a3a3a 45%, #111 72%, transparent 76%); }
  .product--silver { background: radial-gradient(circle at 45% 40%, #ffffff 0%, #dcdcdc 45%, #b9a27a 70%, transparent 74%); }
  .product--rose   { background: radial-gradient(circle at 45% 40%, #f08ad0 0%, #c04aa0 35%, #1a1a1a 65%, transparent 72%); }
  .product--gem    { background: radial-gradient(circle at 45% 40%, #d0387f 0%, #6fb6e6 35%, #8a8a90 62%, transparent 70%); }

  .swoosh { position: absolute; left: 0; top: 0; width: 455px; height: 375px; }
  .swoosh__shade { fill: var(--ink-soft); }
  .swoosh__fill { fill: var(--ink); }

  .offer {
    position: absolute;
    left: 30px; top: 195px;
    color: var(--text-light);
    line-height: 1;
  }
  .offer__lead { display: block; font-size: 30px; font-weight: 400; }
  .offer__value { display: block; font-size: 78px; font-weight: 400; margin-top: 4px; letter-spacing: -1px; }
  .offer__tail { display: block; font-size: 33px; font-weight: 400; margin-top: 2px; }

  .cta {
    position: absolute;
    left: 275px; top: 318px;
    width: 148px; height: 38px;
    background: var(--ink);
    color: var(--text-light);
    font-size: 20px; font-weight: 500; letter-spacing: 1px;
    display: flex; align-items: center; justify-content: center;
  }
</style>
</head>
<body>

<section class="ad ad--a">
  <div class="brand"><span class="brand__mark"></span>BIDMARLOW</div>
  <div class="product product--gold" role="img" aria-label="Gold and silver pavé ring with a large round clear stone"></div>
  <svg class="swoosh" viewBox="0 0 455 375" aria-hidden="true">
    <path class="swoosh__shade" d="M0 140 C160 128 282 230 300 375 L0 375 Z"/>
    <path class="swoosh__fill" d="M0 144 C152 134 270 232 287 375 L0 375 Z"/>
  </svg>
  <p class="offer"><span class="offer__lead">Up To</span><span class="offer__value">80%</span><span class="offer__tail">Off Retail</span></p>
  <div class="cta">VIEW NOW</div>
</section>

<section class="ad ad--b">
  <div class="brand"><span class="brand__mark"></span>BIDMARLOW</div>
  <div class="product product--noir" role="img" aria-label="Black ring set with a pink centre stone and a matching band"></div>
  <svg class="swoosh" viewBox="0 0 455 375" aria-hidden="true">
    <path class="swoosh__shade" d="M0 140 C160 128 282 230 300 375 L0 375 Z"/>
    <path class="swoosh__fill" d="M0 144 C152 134 270 232 287 375 L0 375 Z"/>
  </svg>
  <p class="offer"><span class="offer__lead">Up To</span><span class="offer__value">80%</span><span class="offer__tail">Off Retail</span></p>
  <div class="cta">VIEW NOW</div>
</section>

<section class="ad ad--c">
  <div class="brand"><span class="brand__mark"></span>BIDMARLOW</div>
  <div class="product product--silver" role="img" aria-label="Silver twisted ring with a marquise clear stone and gold filigree"></div>
  <svg class="swoosh" viewBox="0 0 455 375" aria-hidden="true">
    <path class="swoosh__shade" d="M0 140 C160 128 282 230 300 375 L0 375 Z"/>
    <path class="swoosh__fill" d="M0 144 C152 134 270 232 287 375 L0 375 Z"/>
  </svg>
  <p class="offer"><span class="offer__lead">Up To</span><span class="offer__value">80%</span><span class="offer__tail">Off Retail</span></p>
  <div class="cta">VIEW NOW</div>
</section>

<section class="ad ad--d">
  <div class="brand"><span class="brand__mark"></span>BIDMARLOW</div>
  <div class="product product--rose" role="img" aria-label="Black ring set lined with pink stones and a pink centre stone"></div>
  <svg class="swoosh" viewBox="0 0 455 375" aria-hidden="true">
    <path class="swoosh__shade" d="M0 140 C160 128 282 230 300 375 L0 375 Z"/>
    <path class="swoosh__fill" d="M0 144 C152 134 270 232 287 375 L0 375 Z"/>
  </svg>
  <p class="offer"><span class="offer__lead">Up To</span><span class="offer__value">80%</span><span class="offer__tail">Off Retail</span></p>
  <div class="cta">VIEW NOW</div>
</section>

<section class="ad ad--e">
  <div class="brand"><span class="brand__mark"></span>BIDMARLOW</div>
  <div class="product product--gem" role="img" aria-label="Silver ring with a pink centre stone flanked by blue stones and pink pavé"></div>
  <svg class="swoosh" viewBox="0 0 455 375" aria-hidden="true">
    <path class="swoosh__shade" d="M0 140 C160 128 282 230 300 375 L0 375 Z"/>
    <path class="swoosh__fill" d="M0 144 C152 134 270 232 287 375 L0 375 Z"/>
  </svg>
  <p class="offer"><span class="offer__lead">Up To</span><span class="offer__value">80%</span><span class="offer__tail">Off Retail</span></p>
  <div class="cta">VIEW NOW</div>
</section>

</body>
</html>
```